Velmorra Design Group Business Card Design

We need a double-sided business card for our company Velmorra Design Group. Our slogan is "Simple Online Solutions." We are looking for a techy, cutting-edge but simple card that looks modern and sleek. We have a black logo attached and would prefer a lighter background to make our logo stand out. We like nice accents to make it pop out and make our clients remember our card.

On the back side, we just want our logo, slogan and website. Again, something very simple. Make the logo big on the back.

```html
<!DOCTYPE html>
<html lang="en">
<head>
<meta charset="utf-8">
<title>Velmorra Design Group – Business Card</title>
<link rel="stylesheet" href="https://fonts.googleapis.com/css2?family=Michroma&family=Oswald:wght@500;600&display=swap">
<style>
  :root {
    --stage-bg: #e4e4e2;
    --green-light: #6fdc3a;
    --green-mid: #3fb81c;
    --green-dark: #237c0e;
    --green-edge: #8cf05a;
    --blue-light: #2a8fe6;
    --blue-dark: #0a48b0;
    --ink: #15171c;
    --card-white: #ffffff;
    --card-grey: #dcdcdc;
    --mark-grey: #cdcdcd;
    --shadow: rgba(0, 0, 0, 0.28);
  }

  * { margin: 0; padding: 0; box-sizing: border-box; }

  html, body {
    width: 1200px;
    height: 871px;
    overflow: hidden;
  }

  body {
    position: relative;
    background: var(--stage-bg);
  }

  .card {
    position: absolute;
    width: 540px;
    height: 309px;
    border-radius: 26px;
    overflow: hidden;
    box-shadow: 0 14px 30px var(--shadow);
  }

  /* Front side */
  .card-front {
    left: 100px;
    top: 130px;
    display: flex;
    flex-direction: column;
  }

  .band-top {
    height: 58px;
    background: linear-gradient(180deg, var(--green-light), var(--green-mid));
    border-bottom: 2px solid var(--green-edge);
  }

  .band-middle {
    flex: 1;
    background: linear-gradient(180deg, var(--blue-dark), var(--blue-light));
    display: flex;
    align-items: center;
    justify-content: center;
  }

  .band-bottom {
    height: 84px;
    background: linear-gradient(180deg, var(--green-mid), var(--green-dark));
    border-top: 2px solid var(--green-edge);
  }

  .company-name {
    font-family: "Michroma", sans-serif;
    font-size: 30px;
    font-weight: 400;
    color: var(--ink);
    letter-spacing: 0.5px;
    white-space: nowrap;
  }

  /* Back side */
  .card-back {
    left: 560px;
    top: 430px;
    background: radial-gradient(ellipse at 45% 35%, var(--card-white) 55%, var(--card-grey) 100%);
  }

  .back-text {
    position: absolute;
    left: 0;
    right: 0;
    top: 112px;
    text-align: center;
  }

  .slogan {
    font-family: "Oswald", sans-serif;
    font-weight: 600;
    font-size: 26px;
    line-height: 1.2;
    letter-spacing: 2px;
    color: var(--ink);
    text-transform: uppercase;
  }

  .website {
    font-family: "Oswald", sans-serif;
    font-weight: 500;
    font-size: 12px;
    letter-spacing: 1.2px;
    color: var(--ink);
    text-transform: uppercase;
    margin-top: 4px;
  }

  .back-mark {
    position: absolute;
    left: 30px;
    bottom: 22px;
    font-family: "Oswald", sans-serif;
    font-weight: 600;
    font-size: 34px;
    line-height: 1;
    letter-spacing: 1px;
    color: var(--mark-grey);
    white-space: nowrap;
  }
</style>
</head>
<body>
  <section class="card card-front" aria-label="Business card front">
    <div class="band-top"></div>
    <div class="band-middle">
      <h1 class="company-name">Velmorra Design Group</h1>
    </div>
    <div class="band-bottom"></div>
  </section>

  <section class="card card-back" aria-label="Business card back">
    <div class="back-text">
      <p class="slogan">Simple Online Solutions</p>
      <p class="website">www.velmorradesigngroup.com</p>
    </div>
    <p class="back-mark">Velmorra Design Group</p>
  </section>
</body>
</html>
```